Brenmore Plumbing Heating and Electric

We are looking for a basic, but very beautiful and professional looking website. We would like the ability for a customer to request service through our website via a form or email that will be forwarded to us. Other then that just contact info, our history, our rates, and the services we offer.

Look at his page, it is WAY TOO BASIC, but if gives a very general base line idea: http://www.ringquickpipes.example/

http://www.pipevalet.example/norfolk/

http://www.tapwise-williamsburg.example/emergency_plumbing.html

Target Market(s)

Heating, air conditioning, plumbing, natural gas

Industry/Entity Type

Plumbing

Number of Pages Required

4 page

Requirements
Must have
• Professional looking, very high end and modern,
Nice to have
• Would like the ability for client to contact us for service through the website utilizing some type of email.

```html
<!DOCTYPE html>
<html lang="en">
<head>
<meta charset="utf-8">
<title>Brenmore Plumbing Heating and Electric</title>
<link href="https://fonts.googleapis.com/css2?family=Merriweather:wght@400;700&family=Open+Sans:ital,wght@0,400;0,600;0,700;1,600&display=swap" rel="stylesheet">
<style>
  :root {
    --dark: #2b2b2b;
    --accent: #2a9fd8;
    --panel: #1d9ad6;
    --panel-soft: rgba(29, 154, 214, 0.88);
    --wine: #7b2738;
    --navy: #2e4f8a;
    --ink: #1d1d1d;
    --white: #ffffff;
  }
  * { box-sizing: border-box; margin: 0; padding: 0; }
  html, body { width: 862px; height: 1200px; overflow: hidden; }
  body { position: relative; background: var(--white); font-family: "Open Sans", Arial, sans-serif; color: var(--ink); }

  .site-header { position: absolute; left: 0; top: 0; width: 862px; height: 67px; background: var(--dark); }
  .brand { position: absolute; left: 30px; top: 21px; display: flex; align-items: center; gap: 8px; }
  .brand-mark { width: 26px; height: 26px; background: var(--accent); }
  .brand-name { font-weight: 700; font-size: 16px; color: var(--white); }
  .main-nav a { position: absolute; top: 26px; font-size: 14px; color: var(--white); text-decoration: none; }
  .main-nav a.is-active { color: var(--accent); }
  .header-phone { position: absolute; left: 726px; top: 23px; font-size: 14px; color: var(--accent); }

  .hero { position: absolute; left: 0; top: 67px; width: 862px; height: 575px;
    background: linear-gradient(135deg, #8d7466 0%, #b39785 35%, #7e6e66 60%, #5c5452 100%); }
  .hero-title { position: absolute; left: 0; top: 95px; width: 862px; text-align: center;
    font-family: "Merriweather", Georgia, serif; font-weight: 700; font-size: 35px; color: var(--white);
    text-shadow: 0 2px 6px rgba(0,0,0,0.35); }
  .perks { position: absolute; left: 0; top: 238px; width: 353px; height: 111px; background: var(--panel-soft);
    clip-path: polygon(0 0, 100% 0, 93% 100%, 0 100%); list-style: none; padding: 8px 0 0 28px; }
  .perks li { display: flex; align-items: center; gap: 12px; height: 33px; font-weight: 700; font-size: 16.5px; color: var(--white); }
  .perks svg { width: 26px; height: 26px; flex: none; }

  .contact-form { position: absolute; left: 523px; top: 238px; width: 203px; height: 228px; background: var(--panel); }
  .contact-form h2 { margin-top: 10px; text-align: center; font-size: 16.5px; font-weight: 700; color: var(--white); }
  .contact-form input { display: block; width: 170px; height: 30px; margin: 0 0 16px 17px; border: none;
    border-top: 3px solid #d7d7d7; background: var(--white); padding: 0 12px; font-family: inherit; font-size: 10px; font-weight: 600; color: #555; }
  .contact-form input:first-of-type { margin-top: 10px; }
  .contact-form input:last-of-type { margin-bottom: 12px; }
  .contact-form input::placeholder { color: #555; }
  .contact-form button { display: block; width: 131px; height: 29px; margin: 0 0 0 36px; border: none; border-radius: 3px;
    background: var(--wine); color: var(--white); font-family: inherit; font-weight: 700; font-size: 12px; }

  .mascot { position: absolute; left: 52px; top: 704px; width: 230px; height: 222px;
    background: linear-gradient(160deg, #f4f4f6 0%, #c8c8e0 55%, #5dbfa8 100%); }
  .intro { position: absolute; left: 347px; top: 686px; width: 470px; font-size: 11.2px; line-height: 12.1px; color: var(--ink); white-space: nowrap; }
  .reviews-title { position: absolute; left: 346px; top: 798px; font-family: "Merriweather", Georgia, serif; font-weight: 400; font-size: 16.8px; color: var(--navy); }
  .review { position: absolute; top: 846px; width: 240px; font-size: 7.6px; line-height: 9.7px; color: var(--navy); white-space: nowrap; }
  .review cite { display: block; margin-top: 12px; font-style: italic; font-weight: 600; font-size: 8.5px; }

  .site-footer { position: absolute; left: 0; top: 997px; width: 862px; height: 203px; background: var(--dark); }
  .footer-links { position: absolute; left: 225px; top: 36px; list-style: none; }
  .footer-links a { color: var(--white); font-size: 11.5px; line-height: 12px; display: block; }
  .social { position: absolute; top: 37px; width: 49px; height: 49px; box-shadow: 0 2px 4px rgba(0,0,0,0.4); }
  .social-one { left: 346px; background: #3c5a99; }
  .social-two { left: 406px; background: #f2694c; }
  .social-three { left: 469px; background: #22b7ee; }
  .footer-phone { position: absolute; left: 637px; top: 34px; font-size: 13.5px; color: var(--white); }
</style>
</head>
<body>
  <header class="site-header">
    <div class="brand"><span class="brand-mark"></span><span class="brand-name">BrenmorePHE</span></div>
    <nav class="main-nav">
      <a class="is-active" href="#" style="left:281px">Home</a>
      <a href="#" style="left:355px">About us</a>
      <a href="#" style="left:446px">Rates</a>
      <a href="#" style="left:520px">Services</a>
    </nav>
    <div class="header-phone">(999)999-9999</div>
  </header>

  <section class="hero" role="img" aria-label="Photograph of pipe wrenches and a pipe cutter on a tiled floor">
    <h1 class="hero-title">Brenmore Plumbing Heating and Electric</h1>
    <ul class="perks">
      <li><svg viewBox="0 0 26 26"><circle cx="13" cy="13" r="11" fill="none" stroke="#fff" stroke-width="2"/><path d="M7 13l5 5 9-12" fill="none" stroke="#fff" stroke-width="2.2"/></svg>Full garanted</li>
      <li><svg viewBox="0 0 26 26"><circle cx="13" cy="13" r="11" fill="none" stroke="#fff" stroke-width="2"/><path d="M7 13l5 5 9-12" fill="none" stroke="#fff" stroke-width="2.2"/></svg>Open 24 Hours</li>
      <li><svg viewBox="0 0 26 26"><circle cx="13" cy="13" r="11" fill="none" stroke="#fff" stroke-width="2"/><path d="M7 13l5 5 9-12" fill="none" stroke="#fff" stroke-width="2.2"/></svg>Wide range of services</li>
    </ul>
    <form class="contact-form">
      <h2>Contact with us!</h2>
      <input type="text" placeholder="name">
      <input type="tel" placeholder="phone">
      <input type="email" placeholder="email">
      <button type="submit">send us</button>
    </form>
  </section>

  <div class="mascot" role="img" aria-label="Illustration of a cartoon plumber carrying a toolbox"></div>
  <p class="intro">Lorem ipsum dolor sit amet, consectetur adipiscing elit, sed do eiusmod tempor incididunt<br>ut labore et dolore magna aliqua. Ut enim ad minim veniam, quis nostrud exercitation<br>ullamco laboris nisi ut aliquip ex ea commodo consequat. Duis aute irure dolor in<br>reprehenderit in voluptate velit esse cillum dolore eu fugiat nulla pariatur. Excepteur<br>sint occaecat cupidatat non proident, sunt in culpa qui officia deserunt mollit anim id<br>est laborum</p>
  <h2 class="reviews-title">Customer Reviews</h2>
  <blockquote class="review" style="left:346px">Lorem ipsum dolor sit amet, consectetur adipiscing elit,<br>sed do eiusmod tempor incididunt ut labore et dolore<br>magna aliqua. Ut enim ad minim veniam, quis<br>nostrud exercitation ullamco laboris nisi ut aliquip ex ea<br>commodo consequat. Duis aute irure dolor in reprehenderit<br>in voluptate velit esse cillum dolore eu fugiat nulla pariatur.<cite>Marcus L</cite></blockquote>
  <blockquote class="review" style="left:604px">Lorem ipsum dolor sit amet, consectetur adipiscing elit,<br>sed do eiusmod tempor incididunt ut labore et dolore<br>magna aliqua. Ut enim ad minim veniam, quis<br>nostrud exercitation ullamco laboris nisi ut aliquip ex ea<br>commodo consequat. Duis aute irure dolor in reprehenderit<br>in voluptate velit esse cillum dolore eu fugiat nulla pariatur.<cite>Marcus L</cite></blockquote>

  <footer class="site-footer">
    <ul class="footer-links">
      <li><a href="#">home</a></li>
      <li><a href="#">about us</a></li>
      <li><a href="#">rates</a></li>
      <li><a href="#">services</a></li>
    </ul>
    <a class="social social-one" href="#" aria-label="Social profile"></a>
    <a class="social social-two" href="#" aria-label="Social profile"></a>
    <a class="social social-three" href="#" aria-label="Social profile"></a>
    <div class="footer-phone">(999)999-9999</div>
  </footer>
</body>
</html>
```